Halvo KT Biz Card Design

Residential / Commercial/ Emergency

Industry/Entity Type

Residential

Contact Information for Business Card

Tomas Welker
President
PO Box 4827
Marlow Bay, NY 11806
tomas@halvo-kt.com
631.555.0172
855.HALVO.KT
www.halvo-kt.com
FB: Halvo KT
Twitter: HALVO KT

```html
<!DOCTYPE html>
<html lang="en">
<head>
<meta charset="utf-8">
<title>Halvo KT – Business Card</title>
<link rel="stylesheet" href="https://fonts.googleapis.com/css2?family=Tinos:wght@400;700&family=Arimo:ital@1&display=swap">
<style>
  :root {
    --ink: #000000;
    --paper: #ffffff;
    --brand-orange: #ff6a00;
    --rule-red: #e01010;
    --header-black: #000000;
    --card-w: 1200px;
    --card-h: 687px;
  }
  * { margin: 0; padding: 0; box-sizing: border-box; }
  html, body {
    width: var(--card-w);
    height: var(--card-h);
    overflow: hidden;
    background: var(--paper);
  }
  .card {
    position: relative;
    width: var(--card-w);
    height: var(--card-h);
    background: var(--paper);
    border: 1.5px solid var(--ink);
    overflow: hidden;
    color: var(--ink);
  }
  .card__header {
    position: absolute;
    left: 0; top: 0;
    width: 1200px; height: 290px;
  }
  .brand-name {
    position: absolute;
    left: 30px; top: 16px;
    font-family: "Tinos", "Times New Roman", serif;
    font-weight: 700;
    font-size: 100px;
    line-height: 1;
    color: var(--brand-orange);
    white-space: nowrap;
  }
  .person-name,
  .hotline,
  .phone {
    position: absolute;
    font-family: "Tinos", "Times New Roman", serif;
    font-weight: 700;
    font-size: 48px;
    line-height: 1;
    white-space: nowrap;
  }
  .person-name { left: 48px; top: 337px; }
  .hotline { right: 42px; top: 337px; }
  .phone { right: 51px; top: 397px; }
  .address {
    position: absolute;
    left: 48px; top: 405px;
    font-family: "Tinos", "Times New Roman", serif;
    font-size: 36px;
    line-height: 49px;
    font-style: normal;
    white-space: nowrap;
  }
  .email {
    position: absolute;
    left: 0; right: 0; top: 598px;
    text-align: center;
    font-family: "Arimo", Arial, sans-serif;
    font-style: italic;
    font-size: 41px;
    line-height: 1;
  }
</style>
</head>
<body>
  <main class="card">
    <svg class="card__header" viewBox="0 0 1200 290">
      <defs>
        <linearGradient id="craft-tone" x1="0" y1="0" x2="0" y2="1">
          <stop offset="0" stop-color="#1a1a1a"/>
          <stop offset="0.45" stop-color="#8a8a8a"/>
          <stop offset="1" stop-color="#ff6a00"/>
        </linearGradient>
      </defs>
      <rect class="header-band" x="0" y="0" width="1200" height="256" fill="var(--header-black)"/>
      <rect class="header-rule" x="0" y="251" width="1200" height="6" fill="var(--rule-red)"/>
      <rect class="header-illustration" role="img" aria-label="Illustration of an orange quadcopter with spinning white propellers"
            x="10" y="124" width="1180" height="154" rx="24" fill="url(#craft-tone)"/>
    </svg>

    <div class="brand-name">HALVO KT</div>

    <div class="person-name">Tomas Welker</div>
    <address class="address">
      PO Box 4827<br>
      Marlow Bay, NY 11806<br>
      www.halvo-kt.com
    </address>

    <div class="hotline">855.HALVO.KT</div>
    <div class="phone">631-555-0172</div>

    <div class="email">tomas@halvo-kt.com</div>
  </main>
</body>
</html>
```